SaaS startup seeking website design and build on Hovrix.io

Need a website designed and built on Hovrix.io for a new SaaS startup called TenaPod (logo provided).

***The winning designer will be provided with a login to our Hovrix.io subscription to deploy the design - please only submit a design if you are familiar with the Hovrix platform. ***

The business will be selling a cloud-based system for customer success management; a tool to ensure SaaS businesses successfully onboard, retain for renewals, upsell and cross-sell to existing customers. Logo and colour guide provided, pages required in the design:
Home,
Tour,
Pricing,
Blog,
Contact

Require buttons/ forms for
Login,
Sign-up for Trial,
Sign-up for Newsletter,
Request Demo,
Contact Us.

The winning designer will be provided with a login to our Hovrix.io subscription to deploy the design - please only submit a design if you are familiar with the Hovrix platform. Draft designs submitted on trial hovrix accounts will also be considered.

Seek inspiration and placeholder content from https://flexmoria.net/
https://www.quibarra.com/
https://palvenrow.com/

Target Market(s)

SaaS companies

Coding

Coded - Design and coding required

Number of Pages Required

1 page

```html
<!DOCTYPE html>
<html lang="en">
<head>
<meta charset="utf-8">
<title>TenaPod — Customer Success Platform</title>
<link href="https://fonts.googleapis.com/css2?family=Ubuntu:wght@400;500;700&family=Lato:wght@400;700&display=swap" rel="stylesheet">
<style>
:root{
  --stage:#262626;
  --navy:#37598a;
  --navy-deep:#2f4f7e;
  --sky:#3aa3d8;
  --sky-deep:#2a82bd;
  --mist:#f0f0f0;
  --ink:#4a4a4a;
  --white:#ffffff;
}
*{margin:0;padding:0;box-sizing:border-box}
html,body{width:703px;height:1200px;overflow:hidden;background:var(--stage)}
body{position:relative;font-family:"Lato",sans-serif;color:var(--ink)}
.page{position:absolute;left:162px;top:18px;width:796px;height:2442px;background:var(--white);transform:scale(0.4763);transform-origin:0 0;overflow:hidden}
.abs{position:absolute}
.h-font{font-family:"Ubuntu",sans-serif}
.btn{position:absolute;display:flex;align-items:center;justify-content:center;border-radius:12px;font-family:"Lato",sans-serif;font-weight:700;font-size:7px;color:var(--white);letter-spacing:.2px;text-transform:uppercase}
.btn-sky{background:var(--sky)}
.btn-navy{background:var(--navy)}
.btn-ghost{border:1.5px solid var(--white)}
/* header */
.site-header{position:absolute;left:0;top:0;width:796px;height:52px;background:var(--white)}
.brand{position:absolute;display:flex;align-items:center;gap:6px;font-family:"Ubuntu",sans-serif;font-weight:400;color:var(--sky)}
.brand-dot{border-radius:50%;background:var(--sky)}
.nav a{position:absolute;top:20px;font-size:8.5px;color:#555;text-decoration:none}
/* hero */
.hero-title{left:161px;top:128px;width:200px;font-size:19px;line-height:23px;color:var(--white);font-weight:400}
.hero-sub{left:162px;top:207px;width:200px;font-size:8.5px;line-height:11px;color:var(--white)}
.field-pill{position:absolute;border:1.5px solid var(--white);border-radius:12px;color:var(--white);font-size:7px;padding-left:10px;display:flex;align-items:center}
.art{position:absolute}
/* sections */
.sec-title{color:var(--navy);font-weight:700}
.body-copy{font-size:7px;line-height:10.7px;text-align:justify;color:var(--ink)}
.feature{position:absolute;left:383px;width:230px;height:40px}
.feature-icon{position:absolute;left:0;top:0;width:36px;height:36px;border-radius:50%;background:var(--white);box-shadow:0 1px 4px rgba(0,0,0,.12);display:flex;align-items:center;justify-content:center}
.feature-title{position:absolute;left:47px;top:-2px;font-family:"Ubuntu",sans-serif;font-weight:500;font-size:9.5px;color:var(--sky)}
.feature-text{position:absolute;left:46px;top:11px;width:170px;font-size:7px;line-height:10px}
/* pricing */
.plan{position:absolute;top:1517px;width:148px;height:230px;background:var(--white);box-shadow:0 1px 5px rgba(0,0,0,.1);text-align:center}
.plan-name{margin-top:12px;font-family:"Ubuntu",sans-serif;font-weight:700;font-size:15px;color:var(--navy)}
.plan-tag{font-size:6.5px;color:#999;margin-top:3px}
.plan-price{margin-top:10px;height:34px;background:var(--sky);color:var(--white);display:flex;align-items:center;justify-content:center;font-family:"Ubuntu",sans-serif}
.plan-price .cur{font-size:10px;align-self:flex-start;margin-top:7px}
.plan-price .amt{font-size:19px;font-weight:700}
.plan-price .per{font-size:6px;line-height:7px;text-align:left;margin-left:2px}
.plan-list{list-style:none;margin-top:12px;font-size:7px;line-height:16.6px;color:#555}
.plan .btn{left:49px;top:195px;width:50px;height:18px;border-radius:9px;font-size:6px}
/* contact */
.field{position:absolute;background:var(--white);border:1px solid #eee;box-shadow:0 1px 3px rgba(0,0,0,.06);font-size:7px;color:#666;padding:8px 8px}
/* footer */
.foot-col{position:absolute;font-size:6.5px;line-height:10px;color:var(--white)}
.foot-col h4{font-size:7.5px;font-weight:700;margin-bottom:4px}
.social{position:absolute;top:2367px;width:11px;height:11px;border-radius:50%;background:var(--white)}
</style>
</head>
<body>
<div class="page">

  <!-- Header -->
  <header class="site-header">
    <div class="brand" style="left:138px;top:13px;font-size:22px"><span class="brand-dot" style="width:8px;height:8px"></span>tenapod</div>
    <nav class="nav">
      <a style="left:287px">Home</a>
      <a style="left:331px">Tour</a>
      <a style="left:370px">Pricing</a>
      <a style="left:418px">Blog</a>
      <a style="left:457px">Contact</a>
    </nav>
    <div class="btn btn-sky" style="left:505px;top:14px;width:52px;height:22px">Login</div>
    <div class="btn btn-navy" style="left:567px;top:14px;width:98px;height:22px;border:1.5px solid #2d4a73">Sign-up for trial</div>
  </header>

  <!-- Hero -->
  <svg class="abs" style="left:0;top:52px" width="796" height="330" viewBox="0 52 796 330">
    <defs>
      <linearGradient id="heroBg" x1="0" y1="0" x2="0" y2="1">
        <stop offset="0" stop-color="#3a5c8a"/><stop offset="1" stop-color="#2f5a8e"/>
      </linearGradient>
    </defs>
    <path d="M0 52H796V300Q398 440 0 305Z" fill="var(--sky)"/>
    <path d="M0 52H796V240Q560 430 398 372Q220 330 0 245Z" fill="url(#heroBg)"/>
  </svg>
  <h1 class="abs h-font hero-title">Lorem ipsum dolor sit amet, consectetu radipiscing elit</h1>
  <p class="abs hero-sub">Lorem ipsum dolor sit amet, consectetur adi piscing elit, sed do eiusmod tempor incid</p>
  <div class="field-pill" style="left:161px;top:245px;width:129px;height:22px">Email:</div>
  <div class="btn btn-sky btn-ghost" style="left:294px;top:245px;width:83px;height:22px">Get started</div>
  <div class="art" role="img" aria-label="Isometric illustration of people working around a laptop, cloud and server racks" style="left:395px;top:88px;width:315px;height:212px;border-radius:20px;background:radial-gradient(ellipse at 50% 55%,#4fa6e0 0%,#3f7fbf 45%,rgba(58,92,138,0) 75%)"></div>

  <!-- About -->
  <h2 class="abs h-font sec-title" style="left:169px;top:433px;font-size:26px">About Us</h2>
  <p class="abs body-copy" style="left:169px;top:477px;width:245px">At vero eos et accusamus et iusto odio dignissimos ducimus qui blanditiis praesentium voluptatum deleniti atque corrupti quos dolores et quas molestias excepturi sint occaecati cupiditate non provident, similique sunt in culpa qui officia deserunt mollitia animi, id est laborum et dolorum fuga. Et harum quidem rerum facilis est et expedita distinctio. Nam libero tempore, cum soluta nobis est eligendi optio cumque nihil impedit quo minus id quod maxime placeat facere possimus, omnis voluptas assumenda est, omnis dolor repellendus.poribus autem quibusdam</p>
  <div class="btn btn-sky" style="left:169px;top:575px;width:86px;height:22px">Request demo</div>
  <div class="art" role="img" aria-label="Photograph of a team working at laptops" style="left:462px;top:412px;width:162px;height:213px;border-radius:40px;background:linear-gradient(160deg,#8b6b55,#5d7fa6 55%,#3c5f90)"></div>

  <!-- Feature band -->
  <svg class="abs" style="left:0;top:630px" width="796" height="500" viewBox="0 630 796 500">
    <path d="M0 680Q150 660 330 700Q520 740 796 650V1080Q620 1140 430 1080Q220 1000 0 1030Z" fill="var(--mist)"/>
    <path d="M0 680Q200 700 400 700Q600 690 796 650V690Q560 720 400 712Q200 705 0 700Z" fill="#f6f6f6"/>
  </svg>
  <div class="art" role="img" aria-label="Laptop showing the TenaPod dashboard" style="left:42px;top:783px;width:311px;height:177px;border-radius:8px;background:linear-gradient(180deg,#1b1b1b 0%,#2a2a2a 6%,#f4f6f9 7%,#e9edf2 88%,#b9bcc0 92%,#8c8f93 100%)"></div>
  <h2 class="abs h-font sec-title" style="left:385px;top:750px;width:240px;font-size:19px;line-height:23px;font-weight:500">Lorem ipsum dolor site re magna aliqua</h2>
  <p class="abs body-copy" style="left:385px;top:805px;width:245px">At vero eos et accusamus et iusto odio dignissimos ducimus qui blanditiis praesentium voluptatum deleniti atque corrupti quos dolores et quas molestias excepturi sint occaecati cupiditate non provident.</p>
  <div class="feature" style="top:852px">
    <div class="feature-icon"><svg width="12" height="14" viewBox="0 0 12 14"><circle cx="6" cy="5" r="4" fill="none" stroke="var(--sky)" stroke-width="1.6"/><rect x="4" y="9.5" width="4" height="3" rx="1" fill="var(--sky)"/></svg></div>
    <div class="feature-title">At vereos et accusamus etusto</div>
    <div class="feature-text">At vero eos et accusamus et iusto odio dignissi mos ducimus qui blalorem nditiis</div>
  </div>
  <div class="feature" style="top:901px">
    <div class="feature-icon"><svg width="12" height="14" viewBox="0 0 12 14"><path d="M3 6V4a3 3 0 0 1 6 0v2" fill="none" stroke="var(--sky)" stroke-width="1.6"/><rect x="1.5" y="6" width="9" height="7" rx="1" fill="var(--sky)"/></svg></div>
    <div class="feature-title">At vereos et accusamus etusto</div>
    <div class="feature-text">At vero eos et accusamus et iusto odio dignissi mos ducimus qui blalorem nditiis</div>
  </div>
  <div class="feature" style="top:955px">
    <div class="feature-icon"><svg width="12" height="14" viewBox="0 0 12 14"><circle cx="6" cy="4" r="3" fill="var(--sky)"/><path d="M0.5 13.5a5.5 5 0 0 1 11 0Z" fill="var(--sky)"/></svg></div>
    <div class="feature-title">At vereos et accusamus etusto</div>
    <div class="feature-text">At vero eos et accusamus et iusto odio dignissi mos ducimus qui blalorem nditiis</div>
  </div>

  <!-- Trial section -->
  <h2 class="abs h-font sec-title" style="left:169px;top:1148px;width:240px;font-size:19px;line-height:23px;font-weight:500">Lorem ipsum dolor site re magna aliqua</h2>
  <p class="abs body-copy" style="left:169px;top:1205px;width:245px">At vero eos et accusamus et iusto odio dignissimos ducimus qui blanditiis praesentium voluptatum deleniti atque corrupti quos dolores et quas molestias excepturi sint occaecati cupiditate non provident, similique sunt in culpa qui officia deserunt mollitia animi, id est laborum et dolorum fuga. Et harum quidem rerum facilis est et expedita distinctio. Nam libero tempore, cum soluta nobis est eligendi optio cumque nihil impedit quo minus id quod maxime placeat facere possimus, omnis voluptas assumenda est, omnis dolor repellendus.poribus autem quibusdam</p>
  <div class="btn btn-sky" style="left:169px;top:1300px;width:98px;height:22px">Sign-up for trial</div>
  <div class="art" role="img" aria-label="Blue-toned photograph of a person using a smartphone" style="left:462px;top:1136px;width:162px;height:216px;border-radius:40px;background:linear-gradient(160deg,#5b8ee0,#2d6cc4 50%,#4fc3ea)"></div>

  <!-- Pricing -->
  <svg class="abs" style="left:0;top:1390px" width="796" height="450" viewBox="0 1390 796 450">
    <path d="M0 1415Q300 1400 500 1405Q680 1408 796 1395V1800Q600 1850 380 1820Q180 1795 0 1805Z" fill="var(--mist)"/>
  </svg>
  <h2 class="abs h-font sec-title" style="left:0;top:1462px;width:796px;text-align:center;font-size:26px;font-weight:500">Simple, Transparent pricing.</h2>

  <div class="plan" style="left:161px">
    <div class="plan-name">Small</div>
    <div class="plan-tag">Lorem lodipsum dolor sit ame</div>
    <div class="plan-price"><span class="cur">$</span><span class="amt">49</span><span class="per">per<br>month</span></div>
    <ul class="plan-list"><li>Sed ut perspiciatis undeo</li><li>Dte natus error sit voluptate</li><li>Slore accusantium dolor</li><li>Emque lauda dumy ntium tota</li><li>Periam ea duumque isa</li></ul>
    <div class="btn btn-sky">Sign up</div>
  </div>
  <div class="plan" style="left:322px">
    <div class="plan-name">Growth</div>
    <div class="plan-tag">Lorem lodipsum dolor sit ame</div>
    <div class="plan-price"><span class="cur">$</span><span class="amt">99</span><span class="per">per<br>month</span></div>
    <ul class="plan-list"><li>Sed ut perspiciatis undeo</li><li>Dte natus error sit voluptate</li><li>Slore accusantium dolor</li><li>Emque lauda dumy ntium tota</li><li>Periam ea duumque isa</li></ul>
    <div class="btn btn-sky">Sign up</div>
  </div>
  <div class="plan" style="left:484px">
    <div class="plan-name">Large</div>
    <div class="plan-tag">Lorem lodipsum dolor sit ame</div>
    <div class="plan-price"><span class="cur">$</span><span class="amt">199</span><span class="per">per<br>month</span></div>
    <ul class="plan-list"><li>Sed ut perspiciatis undeo</li><li>Dte natus error sit voluptate</li><li>Slore accusantium dolor</li><li>Emque lauda dumy ntium tota</li><li>Periam ea duumque isa</li></ul>
    <div class="btn btn-sky">Sign up</div>
  </div>

  <!-- Contact -->
  <div class="art" style="left:0;top:1890px;width:796px;height:220px;background:linear-gradient(170deg,#ffffff 0%,#eef3f8 55%,#f7f9fb 100%)"></div>
  <h2 class="abs h-font sec-title" style="left:0;top:1856px;width:796px;text-align:center;font-size:26px;font-weight:500">Contact Us</h2>
  <div class="field" style="left:272px;top:1898px;width:252px;height:26px">Name:</div>
  <div class="field" style="left:272px;top:1929px;width:123px;height:26px">Email Address</div>
  <div class="field" style="left:400px;top:1929px;width:124px;height:26px">Phone (Optional)</div>
  <div class="field" style="left:272px;top:1961px;width:252px;height:62px">Your Message</div>
  <div class="btn btn-sky" style="left:357px;top:2037px;width:82px;height:22px">Submit here</div>

  <!-- Call to action -->
  <svg class="abs" style="left:0;top:2070px" width="796" height="230" viewBox="0 2070 796 230">
    <defs>
      <linearGradient id="ctaBg" x1="0" y1="0" x2="1" y2="1">
        <stop offset="0" stop-color="#2e86c0"/><stop offset="1" stop-color="#2a6fae"/>
      </linearGradient>
    </defs>
    <path d="M0 2100Q380 2060 796 2080V2300H0Z" fill="var(--sky)"/>
    <path d="M0 2112Q380 2078 796 2098V2300H0Z" fill="url(#ctaBg)"/>
  </svg>
  <h2 class="abs h-font" style="left:0;top:2149px;width:796px;text-align:center;font-size:18px;font-weight:500;color:var(--white)">Ready to get started?</h2>
  <p class="abs" style="left:215px;top:2177px;width:366px;text-align:center;font-size:7px;line-height:10.5px;color:var(--white)">At vero eos et accusamus et iusto odio dignissimos ducimus qui blanditiis praesentium voluptatum deleniti atque corrupti quos dolores et quas molestias excepturi sint occaecati cupiditate non provide</p>
  <div class="btn btn-navy" style="left:312px;top:2210px;width:81px;height:23px">Get started</div>
  <div class="btn btn-ghost" style="left:399px;top:2210px;width:81px;height:23px">Contact us</div>

  <!-- Footer -->
  <footer class="abs" style="left:0;top:2290px;width:796px;height:152px;background:var(--navy)">
    <div class="brand" style="left:162px;top:32px;font-size:30px;color:#d9d9d9"><span class="brand-dot" style="width:10px;height:10px;background:#d9d9d9"></span>tenapod</div>
    <div class="foot-col" style="left:406px;top:42px"><h4>Product</h4>Features<br>Pricing<br>Tour</div>
    <div class="foot-col" style="left:478px;top:41px"><h4>Company</h4>About<br>Team<br>Blog</div>
    <div class="foot-col" style="left:566px;top:37px"><h4>Legal</h4>Terms of Service<br>Privacy Policy<br>GDPR Policy</div>
    <div class="abs" style="left:0;top:127px;width:796px;text-align:center;font-size:6.5px;color:var(--white)">Copyright © 2020 All Right Reserved.</div>
  </footer>
  <span class="social" style="left:159px"></span>
  <span class="social" style="left:186px"></span>
  <span class="social" style="left:213px"></span>
  <span class="social" style="left:240px"></span>

</div>
</body>
</html>
```